Awesome Business Card and stationary Project!
Attorney
Awesome Business Card and stationary Project! -
Creative Brief
Professional
Rosalind T. Dalwyn
Attorney at Law
5182 N. Brookfield Lane, Ste. 416 Las Vegas NV 89147
rdalwyn@rdalwynlegal.example
www.rdalwynlegal.example
Please use our logo and font...have fun Stationary and business cards: we are completey open to ideas as to where the info should be located
RTD logo on the back. At the bottom: Offices in Las Vegas, NV and San Diego, CA

```html
<!DOCTYPE html>
<html lang="en">
<head>
<meta charset="utf-8">
<title>Rosalind T. Dalwyn — Stationery Set</title>
<link rel="stylesheet" href="https://fonts.googleapis.com/css2?family=Cormorant+Garamond:wght@500;600&family=Lato:wght@400;700&display=swap">
<style>
:root{
  --bg:#ece5db;
  --paper:#ffffff;
  --green-dark:#3f5a24;
  --green:#6d8a45;
  --grey:#6e6e6e;
  --grey-light:#a9a9a9;
  --ink:#3b3b3b;
  --mark:#3a3a3a;
  --watermark:#efefef;
  --caption:#8a7f70;
}
*{box-sizing:border-box;margin:0;padding:0}
html,body{width:1200px;height:346px;overflow:hidden;background:var(--bg)}
body{position:relative;font-family:"Lato",sans-serif;color:var(--ink)}
.piece{position:absolute;background:var(--paper);box-shadow:0 1px 3px rgba(0,0,0,.25);overflow:hidden}
.piece .swoosh{position:absolute;left:0;top:0;width:100%}
.caption{position:absolute;font-size:5px;letter-spacing:.5px;text-transform:uppercase;color:var(--caption)}
.mark{display:flex;align-items:center;gap:2px;font-family:"Cormorant Garamond",serif;font-weight:600;color:var(--mark);position:absolute}
.mark i{display:block;background:var(--mark)}
.watermark{position:absolute;font-family:"Cormorant Garamond",serif;font-weight:600;color:var(--watermark);letter-spacing:2px}
.firm{position:absolute;font-family:"Cormorant Garamond",serif;font-size:5px;color:var(--ink);text-align:center}
.detail{position:absolute;font-size:3.4px;line-height:1.5;color:var(--grey)}
.footer{position:absolute;left:0;right:0;text-align:center;font-size:3.4px;color:var(--grey)}
</style>
</head>
<body>

<!-- business cards -->
<span class="caption" style="left:12px;top:66px">business cards</span>
<div class="piece card card-front" style="left:12px;top:77px;width:108px;height:66px">
  <svg class="swoosh" viewBox="0 0 108 20" height="20" preserveAspectRatio="none"><path d="M0 0H108V6Q60 18 0 12Z" fill="var(--green-dark)"/><path d="M0 12Q60 18 108 6V8Q60 20 0 14Z" fill="var(--green)"/></svg>
  <div class="mark" style="left:8px;top:26px;font-size:9px"><i style="width:5px;height:5px"></i>RTD</div>
  <div class="detail" style="left:8px;top:40px">Rosalind T. Dalwyn · Attorney at Law<br>5182 N. Brookfield Lane, Ste. 416<br>Las Vegas NV 89147<br>rdalwyn@rdalwynlegal.example</div>
</div>
<div class="piece card card-back" style="left:12px;top:156px;width:108px;height:66px">
  <div class="watermark" style="left:30px;top:16px;font-size:28px">RTD</div>
  <div class="detail" style="left:0;right:0;bottom:4px;text-align:center">Offices in Las Vegas, NV and San Diego, CA</div>
</div>

<!-- letterhead -->
<span class="caption" style="left:156px;top:4px">letterhead</span>
<div class="piece letterhead" style="left:156px;top:12px;width:199px;height:308px">
  <svg class="swoosh" viewBox="0 0 199 34" height="34" preserveAspectRatio="none"><path d="M0 0H199V6Q110 34 0 24Z" fill="var(--green-dark)"/><path d="M0 24Q110 34 199 6V9Q110 37 0 27Z" fill="var(--green)"/></svg>
  <div class="mark" style="left:87px;top:3px;font-size:9px;color:#fff"><i style="width:5px;height:5px;background:#fff"></i>RTD</div>
  <div class="firm" style="left:0;right:0;top:16px;color:#fff">Rosalind T. Dalwyn, Attorney at Law</div>
  <div class="watermark" style="left:36px;top:168px;font-size:58px">RTD</div>
  <div class="detail" style="left:22px;top:258px">5182 N. Brookfield Lane, Ste. 416<br>Las Vegas NV 89147<br>www.rdalwynlegal.example</div>
  <div class="footer" style="bottom:6px">Offices in Las Vegas, NV and San Diego, CA</div>
</div>

<!-- second sheet -->
<span class="caption" style="left:367px;top:4px">second sheet</span>
<div class="piece second-sheet" style="left:367px;top:12px;width:202px;height:308px">
  <div class="mark" style="left:88px;top:16px;font-size:9px"><i style="width:5px;height:5px"></i>RTD</div>
  <div class="firm" style="left:0;right:0;top:29px">Rosalind T. Dalwyn, Attorney at Law</div>
  <div class="watermark" style="left:38px;top:70px;font-size:58px">RTD</div>
  <div class="footer" style="bottom:10px">5182 N. Brookfield Lane, Ste. 416 · Las Vegas NV 89147 · rdalwyn@rdalwynlegal.example</div>
</div>

<!-- #10 envelopes -->
<span class="caption" style="left:617px;top:26px">#10 envelope</span>
<div class="piece envelope" style="left:617px;top:36px;width:211px;height:113px">
  <svg class="swoosh" viewBox="0 0 211 30" height="30" preserveAspectRatio="none"><path d="M0 0H211V4Q120 30 0 20Z" fill="var(--green-dark)"/><path d="M0 20Q120 30 211 4V7Q120 33 0 23Z" fill="var(--green)"/></svg>
  <div class="mark" style="left:10px;top:3px;font-size:8px;color:#fff"><i style="width:4px;height:4px;background:#fff"></i>RTD</div>
  <div class="detail" style="left:10px;top:14px;color:#fff">5182 N. Brookfield Lane, Ste. 416<br>Las Vegas NV 89147</div>
</div>
<div class="piece envelope" style="left:617px;top:173px;width:211px;height:96px">
  <svg class="swoosh" viewBox="0 0 211 30" height="30" preserveAspectRatio="none"><path d="M0 0H211V4Q120 30 0 20Z" fill="var(--green-dark)"/><path d="M0 20Q120 30 211 4V7Q120 33 0 23Z" fill="var(--green)"/></svg>
  <div class="mark" style="left:10px;top:3px;font-size:8px;color:#fff"><i style="width:4px;height:4px;background:#fff"></i>RTD</div>
  <div class="detail" style="left:10px;top:14px;color:#fff">5182 N. Brookfield Lane, Ste. 416<br>Las Vegas NV 89147</div>
</div>

<!-- envelope flap options -->
<span class="caption" style="left:845px;top:300px">envelope options</span>
<div class="flap-set" style="position:absolute;left:845px;top:24px;width:211px">
  <svg width="211" height="260" viewBox="0 0 211 260">
    <rect x="0" y="0" width="211" height="72" fill="var(--paper)"/>
    <path d="M0 0H211L196 30H15Z" fill="var(--green-dark)"/>
    <rect x="0" y="84" width="211" height="84" fill="var(--paper)"/>
    <path d="M0 84H211L196 116Q105 126 15 116Z" fill="var(--grey)"/>
    <rect x="0" y="173" width="211" height="86" fill="var(--paper)"/>
    <path d="M0 173H211L181 203H30Z" fill="var(--paper)" stroke="var(--grey-light)" stroke-width=".8"/>
  </svg>
  <div class="mark" style="left:92px;top:9px;font-size:10px;color:#fff"><i style="width:5px;height:5px;background:#fff"></i>RTD</div>
  <div class="mark" style="left:92px;top:95px;font-size:10px;color:#fff"><i style="width:5px;height:5px;background:#fff"></i>RTD</div>
  <div class="mark" style="left:92px;top:182px;font-size:10px;color:var(--green-dark)"><i style="width:5px;height:5px;background:var(--green-dark)"></i>RTD</div>
</div>

</body>
</html>
```